E-Waste Recycling Company Business Card

New Electronic Recycling Company based in Long Island, New York called "Lady Rust-a-bunch" We take outdated computers, components, electrical wire, circuit breakers, ink cartridges, etc. We look mostly for donated items that we recycle for our customers but will pay for large quantities from businesses. The design should reflect that we are environmentally friendly and our unique 7Q Obliteration process that ensures all personal data is wiped clean off hard drives. Please use our attached logo
Industry/Entity Type
Electrical

```html
<!DOCTYPE html>
<html lang="en">
<head>
<meta charset="utf-8">
<title>Lady Rust-a-bunch Business Card</title>
<link rel="stylesheet" href="https://fonts.googleapis.com/css2?family=Cinzel:wght@700&family=Roboto:wght@400&display=swap">
<style>
  :root {
    --green: #7cc142;
    --green-dark: #3f8f1f;
    --grey: #7b7b7b;
    --ink: #1b1b1b;
    --paper: #ffffff;
    --backdrop: #ecebe8;
  }
  * { box-sizing: border-box; margin: 0; padding: 0; }
  html, body { width: 1200px; height: 905px; overflow: hidden; background: var(--backdrop); }
  .canvas { position: relative; width: 1200px; height: 905px; }

  .card {
    position: absolute; width: 580px; height: 330px; overflow: hidden;
    box-shadow: 0 6px 18px rgba(0,0,0,.18);
  }
  .serif { font-family: "Cinzel", Georgia, serif; font-weight: 700; }
  .sans { font-family: "Roboto", Arial, sans-serif; }

  /* Back card */
  .card-back { left: 60px; top: 60px; background: var(--grey); }
  .card-back svg.wave { position: absolute; inset: 0; }
  .brand-mark {
    position: absolute; left: 200px; top: 70px; width: 180px;
    display: flex; flex-direction: column; align-items: center; gap: 8px;
    text-align: center; color: var(--ink); font-size: 17px; line-height: 1.15;
  }
  .brand-dot { width: 34px; height: 34px; border-radius: 50%; background: var(--paper); }
  .materials { position: absolute; color: var(--ink); font-size: 16px; line-height: 1.25; letter-spacing: .3px; }
  .materials-left { left: 34px; top: 212px; }
  .materials-right { right: 34px; top: 150px; text-align: left; }

  /* Front card */
  .card-front { left: 560px; top: 470px; background: var(--paper); }
  .person { position: absolute; left: 44px; top: 70px; }
  .person-name { color: var(--green); font-size: 22px; letter-spacing: .5px; }
  .person-role { font-size: 14px; color: var(--ink); margin-top: 2px; }
  .contacts { position: absolute; left: 44px; top: 136px; list-style: none; font-size: 17px; color: var(--ink); }
  .contacts li { display: flex; align-items: center; gap: 8px; height: 24px; }
  .contacts svg { width: 15px; height: 15px; flex: none; }
  .address { position: absolute; left: 44px; top: 240px; font-size: 17px; line-height: 1.3; color: var(--ink); font-style: normal; }
  .front-brand {
    position: absolute; right: 40px; top: 80px; width: 210px;
    display: flex; flex-direction: column; align-items: center; gap: 12px;
    text-align: center; color: var(--ink); font-size: 24px; line-height: 1.15;
  }
  .front-brand .brand-dot { width: 44px; height: 44px; background: var(--green); }
</style>
</head>
<body>
<main class="canvas">

  <section class="card card-back" aria-label="Business card back">
    <svg class="wave" width="580" height="330" viewBox="0 0 580 330" aria-hidden="true">
      <path d="M0,205 Q300,200 580,60 L580,330 L0,330 Z" fill="var(--green)"/>
    </svg>
    <div class="brand-mark serif">
      <span class="brand-dot" aria-hidden="true"></span>
      <span>Lady Rust-a-bunch</span>
    </div>
    <p class="materials materials-left serif">Outdated computers,<br>components,<br>electrical wire,</p>
    <p class="materials materials-right serif">Circuit breakers<br>ink cartridges</p>
  </section>

  <section class="card card-front" aria-label="Business card front">
    <div class="person">
      <h1 class="person-name serif">Mara Vellin</h1>
      <p class="person-role sans">Director</p>
    </div>
    <ul class="contacts sans">
      <li>
        <svg viewBox="0 0 16 16" aria-hidden="true"><path fill="var(--green-dark)" d="M3 2l3 0 1 3-2 1.5c1 2 2.5 3.5 4.5 4.5L11 9l3 1v3c0 .6-.4 1-1 1C7 14 2 9 2 3c0-.6.4-1 1-1z"/></svg>
        +1 555-014-2290
      </li>
      <li>
        <svg viewBox="0 0 16 16" aria-hidden="true"><rect x="1" y="3" width="14" height="10" rx="1" fill="var(--green-dark)"/><path d="M1.5 4l6.5 5 6.5-5" stroke="#fff" stroke-width="1.4" fill="none"/></svg>
        rustabunch@mailhub.net
      </li>
      <li>
        <svg viewBox="0 0 16 16" aria-hidden="true"><circle cx="8" cy="8" r="7" fill="var(--green-dark)"/><path d="M1 8h14M8 1c-3 3-3 11 0 14M8 1c3 3 3 11 0 14" stroke="#fff" stroke-width="1" fill="none"/></svg>
        www.rustabunch.net
      </li>
    </ul>
    <address class="address sans">18 Cedar Bend Ln<br>Harbor Glen, New York</address>
    <div class="front-brand serif">
      <span class="brand-dot" aria-hidden="true"></span>
      <span>Lady Rust-a-bunch</span>
    </div>
  </section>

</main>
</body>
</html>
```